IT Consulting, IT Guru, Software Development, Network Solutions, Hosting

Attached is logo for our company, we just was the designers to come up with creative ideas to use the logo and the theme to come with creative and energetic business cards that leave an impression and stick in people's head.

Target Market(s)

Medical, Law, Entertainment, Real estate, any small to medium size business.

Industry/Entity Type

Business

Font styles to use
Serif
Sans Serif

```html
<!DOCTYPE html>
<html lang="en">
<head>
<meta charset="utf-8">
<title>BYTEFORGE Business Cards</title>
<link rel="stylesheet" href="https://fonts.googleapis.com/css2?family=Open+Sans:ital,wght@0,400;0,600;1,400&display=swap">
<style>
  :root {
    --page: #e6e6e4;
    --card: #383838;
    --strip: #323232;
    --yellow: #ffd200;
    --line-light: #d9d9d9;
    --line-mid: #a9a9a9;
    --text: #f2f2f2;
    --shadow: rgba(0, 0, 0, 0.28);
  }
  * { box-sizing: border-box; margin: 0; padding: 0; }
  html, body {
    width: 1200px;
    height: 900px;
    overflow: hidden;
    background: var(--page);
    font-family: "Open Sans", Arial, sans-serif;
  }
  .sheet {
    width: 1200px;
    height: 900px;
    display: flex;
    flex-direction: column;
    align-items: center;
    justify-content: center;
    gap: 36px;
  }
  .card {
    position: relative;
    width: 700px;
    height: 400px;
    background: var(--card);
    box-shadow: 0 8px 20px var(--shadow);
    overflow: hidden;
  }
  .brand {
    position: absolute;
    font-weight: 600;
    font-size: 46px;
    letter-spacing: 2px;
    color: var(--yellow);
    line-height: 1;
  }
  .card--front .brand { left: 90px; top: 72px; }
  .card--back .brand { left: 0; right: 0; top: 150px; text-align: center; }

  .contact-strip {
    position: absolute;
    left: 0; right: 0;
    top: 196px;
    height: 84px;
    background: var(--strip);
    display: grid;
    grid-template-columns: 1.15fr 1fr 1.2fr;
    grid-template-rows: 1fr 1fr;
    padding: 14px 30px 10px 48px;
    column-gap: 20px;
  }
  .contact-item {
    display: flex;
    align-items: center;
    gap: 8px;
    font-style: italic;
    font-size: 13px;
    color: var(--text);
    white-space: nowrap;
  }
  .contact-item svg { width: 13px; height: 13px; flex: none; }

  .rule-band {
    position: absolute;
    left: 0; right: 0;
    height: 16px;
    background: repeating-linear-gradient(
      to bottom,
      var(--line-light) 0 1px,
      var(--line-mid) 1px 2px
    );
  }
  .yellow-band {
    position: absolute;
    left: 0; right: 0; bottom: 0;
    height: 104px;
    background: var(--yellow);
  }
  .card--front .rule-band,
  .card--back .rule-band { bottom: 104px; }
</style>
</head>
<body>
<main class="sheet">

  <section class="card card--front" aria-label="Business card front">
    <div class="brand">BYTEFORGE</div>

    <div class="contact-strip">
      <div class="contact-item">
        <svg viewBox="0 0 12 12" fill="#ffd200"><circle cx="6" cy="3.5" r="2.6"/><path d="M1 12c0-3.5 2-5 5-5s5 1.5 5 5z"/></svg>
        Name and Surname
      </div>
      <div class="contact-item">
        <svg viewBox="0 0 12 12" fill="#ffd200"><path d="M2.5 1l2 2.5-1.2 1.3c.8 1.6 2.1 2.9 3.7 3.7l1.3-1.2L11 9.5 9.6 11C5 10.5 1.5 7 1 2.4z"/></svg>
        Telephone
      </div>
      <div class="contact-item">
        <svg viewBox="0 0 12 12" fill="none" stroke="#ffd200" stroke-width="1.4"><circle cx="6" cy="6" r="5"/><path d="M1 6h10M6 1c2 2 2 8 0 10M6 1c-2 2-2 8 0 10"/></svg>
        www.yourwebsite.com
      </div>
      <div class="contact-item">
        <svg viewBox="0 0 12 12" fill="#ffd200"><path d="M6 0C3.5 0 2 1.8 2 4c0 3 4 8 4 8s4-5 4-8c0-2.2-1.5-4-4-4zm0 5.5A1.5 1.5 0 1 1 6 2.5a1.5 1.5 0 0 1 0 3z"/></svg>
        Address
      </div>
      <div class="contact-item">
        <svg viewBox="0 0 12 12" fill="#ffd200"><rect x="3" y="1" width="6" height="4"/><rect x="1" y="5" width="10" height="5" rx="1"/><rect x="3" y="9" width="6" height="3"/></svg>
        Fax
      </div>
      <div class="contact-item">
        <svg viewBox="0 0 12 12" fill="none" stroke="#ffd200" stroke-width="1.3"><rect x="0.7" y="2" width="10.6" height="8"/><path d="M0.7 2l5.3 4.5L11.3 2"/></svg>
        your@email.com
      </div>
    </div>

    <div class="rule-band"></div>
    <div class="yellow-band"></div>
  </section>

  <section class="card card--back" aria-label="Business card back">
    <div class="brand">BYTEFORGE</div>
    <div class="rule-band"></div>
    <div class="yellow-band"></div>
  </section>

</main>
</body>
</html>
```